hfdhddfgfhfghfghgfhfhfhgfhfhfh

Industry/Entity Type

Painting

Logo Text

KOLBEC Painting

Logo styles of interest
Wordmark Logo
Requirements
Should not have
• Paintbrushes or rollers etc....

```html
<!DOCTYPE html>
<html lang="en">
<head>
<meta charset="utf-8">
<title>KOLBEC Painting – Business Card</title>
<link rel="stylesheet" href="https://fonts.googleapis.com/css2?family=Arimo:wght@400;700&family=PT+Serif:wght@700&display=swap">
<style>
  :root {
    --stage: #1b1b1b;
    --card-front: #f9f9f9;
    --brand-blue: #0d4fa0;
    --accent-cyan: #1aa7d0;
    --sky-edge: #a9dcea;
    --sky-mid: #d8f0f7;
    --ink-dark: #3f3f3f;
    --ink-mid: #555555;
  }
  * { margin: 0; padding: 0; box-sizing: border-box; }
  html, body { width: 951px; height: 1200px; overflow: hidden; }
  body {
    background: var(--stage);
    position: relative;
    font-family: "Arimo", Arial, sans-serif;
  }
  .card {
    position: absolute;
    left: 67px;
    width: 817px;
    height: 503px;
    overflow: hidden;
  }
  .card--front { top: 84px; background: var(--card-front); }
  .card--back {
    top: 612px;
    background: radial-gradient(ellipse 75% 85% at 58% 25%, #ffffff 0%, var(--sky-mid) 55%, var(--sky-edge) 100%);
  }

  .brand-name {
    position: absolute;
    color: var(--brand-blue);
    font-weight: 700;
    line-height: 1;
    text-align: center;
    white-space: nowrap;
  }
  .tagline {
    position: absolute;
    color: var(--ink-dark);
    letter-spacing: 0.06em;
    text-align: center;
    white-space: nowrap;
  }

  .card--front .brand-name { left: 0; width: 100%; top: 196px; font-size: 54px; }
  .card--front .tagline { left: 0; width: 100%; top: 278px; font-size: 19px; }

  .front-rule { position: absolute; left: 173px; top: 410px; width: 466px; height: 4px; }
  .site-url {
    position: absolute; left: 0; width: 100%; top: 436px;
    text-align: center; font-family: "PT Serif", Georgia, serif;
    font-weight: 700; font-size: 20px; color: var(--ink-mid);
  }

  .back-band { position: absolute; left: 0; top: 112px; width: 388px; height: 94px; background: var(--brand-blue); }
  .card--back .brand-name { left: 424px; width: 338px; top: 134px; font-size: 36px; }
  .card--back .tagline { left: 424px; width: 338px; top: 201px; font-size: 15px; letter-spacing: 0.05em; }

  .divider { position: absolute; left: 410px; top: 293px; width: 2px; height: 164px; }

  .person { position: absolute; left: 61px; top: 366px; }
  .person__name { font-size: 28px; font-weight: 700; color: var(--ink-dark); line-height: 1.1; }
  .person__role { font-size: 20px; color: var(--ink-mid); margin-top: 4px; }

  .contact {
    position: absolute; right: 63px; top: 340px;
    text-align: right; font-size: 20px; line-height: 29px; color: var(--ink-mid);
    list-style: none;
  }
</style>
</head>
<body>
  <section class="card card--front" aria-label="Card front">
    <p class="brand-name">KOLBEC Painting</p>
    <p class="tagline">Domestic, Residential &amp; Commercial</p>
    <svg class="front-rule" viewBox="0 0 466 4" preserveAspectRatio="none" aria-hidden="true">
      <defs>
        <linearGradient id="ruleFade" x1="0" x2="1">
          <stop offset="0" stop-color="#6a6a6a" stop-opacity="0"/>
          <stop offset="0.15" stop-color="#6a6a6a"/>
          <stop offset="0.85" stop-color="#6a6a6a"/>
          <stop offset="1" stop-color="#6a6a6a" stop-opacity="0"/>
        </linearGradient>
      </defs>
      <ellipse cx="233" cy="2" rx="233" ry="2" fill="url(#ruleFade)"/>
    </svg>
    <p class="site-url">www.kolbecpainting.com</p>
  </section>

  <section class="card card--back" aria-label="Card back">
    <div class="back-band"></div>
    <p class="brand-name">KOLBEC Painting</p>
    <p class="tagline">Domestic, Residential &amp; Commercial</p>
    <svg class="divider" viewBox="0 0 2 164" preserveAspectRatio="none" aria-hidden="true">
      <defs>
        <linearGradient id="dividerFade" x1="0" y1="0" x2="0" y2="1">
          <stop offset="0" stop-color="#1aa7d0" stop-opacity="0"/>
          <stop offset="0.5" stop-color="#1aa7d0"/>
          <stop offset="1" stop-color="#1aa7d0" stop-opacity="0"/>
        </linearGradient>
      </defs>
      <rect width="2" height="164" fill="url(#dividerFade)"/>
    </svg>
    <div class="person">
      <p class="person__name">Lukas Brenner</p>
      <p class="person__role">Managing Director</p>
    </div>
    <ul class="contact">
      <li>mobile : 0412555318</li>
      <li>ABN: 51 824 753 556</li>
      <li>kolbecpainting@example.com</li>
    </ul>
  </section>
</body>
</html>
```